Curtain Cleaning Flyer to be designed for Singapore market

We are a laundry company providing curtain cleaning services to Singapore market. We have a company vehicle pickup and provide dismantling of curtain at customer house. The dismantled curtain will be weighed and quote will be given to customer immediately. If they accept the price, we will delivered and installed the clean curtain to them.
Refer to our website for more information https://www.glimmerloft.com.sg/curtain-cleaning
The flyer will be distributed to higher income level people in Singapore staying in condominium/semi detached or bungalow.
I need a well designed flyers to engage people to use my service. So please help.

Target Market(s)

Singapore market

Industry/Entity Type

It Company

Requirements
Must have
• MUST INCLUDE CURTAINS pictures in design to let people know it is for curtain laundry
• 1) Flyer has to be eye catching and engage people to call and use our curtain cleaning services.
• 2) It has to professional.
• 3) It has to provide clear information of the following (see curtain cleaning picture I have provided)
• Curtain Laundry at $10/kg
• Call 8614 2253
• No Hidden Cost
• Include Pickup, Dismantle, Installation and Delivery
• 4) Provide company information:
• GLIMMER LOFT, Reg No.71840362K
• 47 Kelvin Brook Road
• Singapore 073194
• https://www.glimmerloft.com.sg/curtain-cleaning
• Email: enquiries@glimmerloft.com.sg
• Tel: +65 8614 2253
• 5) Include our company logo but do not use it extensively.
Nice to have
• Nice to have a compelling action design for people to call and use my service.
• Nice to highlight on the good laundry price $10 per kg for curtain laundry
• Nice to be professional and cute
Should not have
• Complicated
• No design on woman wearing low cut dresses for promotion

```html
<!DOCTYPE html>
<html lang="en">
<head>
<meta charset="utf-8">
<title>Glimmer Loft – Curtain Cleaning</title>
<link href="https://fonts.googleapis.com/css2?family=Cabin:wght@700&family=Questrial&family=Fira+Sans+Condensed:wght@500&display=swap" rel="stylesheet">
<style>
  :root {
    --curtain-blue-dark: #0f4f7a;
    --curtain-blue: #2a8fc4;
    --band-navy: #233f8f;
    --band-sky: #3aa6e0;
    --machine-grey: #d9dadc;
    --machine-shade: #8d9196;
    --fabric: #b9b2a9;
    --card-bg: #f8f6f0;
    --header-navy: #2a5596;
    --header-navy-deep: #1d3f78;
    --ink: #111;
    --row-ink: #3b3b3b;
    --rule: #c9c6bf;
    --info-bg: #a9d2e6;
    --info-ink: #1c4b82;
    --white: #fff;
  }
  * { margin: 0; padding: 0; box-sizing: border-box; }
  html, body { width: 746px; height: 1200px; overflow: hidden; }
  body { position: relative; background: var(--machine-grey); font-family: 'Questrial', sans-serif; }

  .backdrop-curtain {
    position: absolute; left: 0; top: 0; width: 746px; height: 640px;
    background: linear-gradient(90deg, var(--curtain-blue-dark) 0%, var(--curtain-blue) 18%, var(--curtain-blue-dark) 34%, var(--curtain-blue) 52%, var(--curtain-blue-dark) 70%, var(--curtain-blue) 86%, var(--curtain-blue-dark) 100%);
  }
  .backdrop-machine {
    position: absolute; left: 0; top: 640px; width: 746px; height: 560px;
    background: radial-gradient(circle at 400px 300px, #3d4650 0 180px, var(--machine-shade) 182px 220px, #eceded 232px 300px, var(--machine-grey) 340px, #b9bbbe 100%);
  }
  .deco { position: absolute; left: 0; top: 0; }

  .brand {
    position: absolute; left: 26px; top: 150px;
    transform: rotate(-14deg); transform-origin: left center;
    display: flex; align-items: center; gap: 10px;
    font-family: 'Cabin', sans-serif; font-weight: 700; font-size: 34px;
    color: var(--white); letter-spacing: 1px;
  }
  .brand-dot { width: 18px; height: 18px; border-radius: 50%; background: var(--white); }

  .service-title {
    position: absolute; left: 30px; top: 368px;
    transform: rotate(-20deg); transform-origin: left bottom;
    font-size: 37px; color: var(--ink); letter-spacing: 1px; white-space: nowrap;
  }

  .offer-card {
    position: absolute; left: 170px; top: 372px; width: 422px; height: 592px;
    background: var(--card-bg);
  }
  .offer-header {
    position: absolute; left: 10px; top: 0; width: 402px; height: 172px;
  }
  .offer-header svg { position: absolute; inset: 0; }
  .offer-price {
    position: relative; padding-top: 22px; text-align: center;
    font-family: 'Cabin', sans-serif; font-weight: 700; font-size: 40px; line-height: 50px; color: var(--ink);
  }
  .offer-list { position: absolute; left: 0; top: 200px; width: 422px; list-style: none; }
  .offer-list li {
    height: 66px; padding-left: 54px; display: flex; align-items: center;
    font-size: 28px; letter-spacing: 1.5px; color: var(--row-ink);
    border-bottom: 1.5px dashed var(--rule);
  }
  .offer-list li.lead { height: 58px; font-size: 32px; }
  .offer-list li:last-child { border-bottom: none; }

  .delivery-van {
    position: absolute; left: 400px; top: 826px; width: 224px; height: 122px;
    background: linear-gradient(180deg, #2f7fd0, #1a55a3); border-radius: 14px 8px 22px 22px;
  }
  .delivery-sign {
    position: absolute; left: 74px; top: 12px; width: 136px; height: 56px;
    background: var(--white); border-radius: 3px; text-align: center;
    font-family: 'Cabin', sans-serif; font-weight: 700; color: #222; line-height: 1;
  }
  .delivery-sign .big { font-size: 30px; display: block; padding-top: 4px; }
  .delivery-sign .small { font-size: 17px; letter-spacing: 1px; }

  .company-info {
    position: absolute; left: 170px; top: 964px; width: 432px; height: 236px;
    background: var(--info-bg); color: var(--info-ink); text-align: center;
    font-family: 'Fira Sans Condensed', sans-serif; font-weight: 500; text-transform: uppercase;
  }
  .company-info p { line-height: 1; }
  .info-reg { font-size: 22px; padding-top: 8px; }
  .info-street { font-size: 22px; padding-top: 10px; }
  .info-city { font-size: 26px; padding-top: 6px; }
  .info-web { font-size: 17.5px; padding-top: 28px; letter-spacing: -0.2px; }
  .info-mail { font-size: 17.5px; padding-top: 9px; }
  .info-tel { font-size: 35px; padding-top: 18px; }
</style>
</head>
<body>
  <div class="backdrop-curtain" role="img" aria-label="Blue draped curtain backdrop with soap bubbles"></div>
  <div class="backdrop-machine" role="img" aria-label="Front-loading washing machine door"></div>

  <svg class="deco" width="746" height="640" viewBox="0 0 746 640">
    <path d="M0 104 L430 0 L470 0 L470 206 L0 322 Z" fill="var(--band-navy)"/>
    <path d="M0 322 L470 206 L500 300 L0 420 Z" fill="var(--band-sky)"/>
    <path role="img" aria-label="Photo of a champagne damask curtain tied back" d="M390 0 L746 0 L746 460 C600 455 490 380 440 280 C400 200 385 100 390 0 Z" fill="var(--fabric)"/>
  </svg>

  <div class="brand"><span class="brand-dot"></span>GLIMMER LOFT</div>
  <div class="service-title">CURTAIN CLEANING</div>

  <section class="offer-card">
    <div class="offer-header">
      <svg width="402" height="172" viewBox="0 0 402 172">
        <path d="M0 0 H402 V132 C300 150 260 172 201 172 C142 172 102 150 0 132 Z" fill="var(--header-navy-deep)"/>
        <path d="M10 0 H392 V124 C292 142 256 160 201 160 C146 160 110 142 10 124 Z" fill="var(--header-navy)"/>
      </svg>
      <h1 class="offer-price">Curtain Laundry<br>at $10/kg</h1>
    </div>
    <ul class="offer-list">
      <li class="lead">No Hidden Cost</li>
      <li>INCLUDE:</li>
      <li>Pickup</li>
      <li>Dismantle</li>
      <li>Installation</li>
      <li>Delivery</li>
    </ul>
  </section>

  <div class="delivery-van" role="img" aria-label="Blue delivery van">
    <div class="delivery-sign"><span class="big">FREE</span><span class="small">DELIVERY</span></div>
  </div>

  <footer class="company-info">
    <p class="info-reg">Reg No.71840362K</p>
    <p class="info-street">47 Kelvin Brook Road</p>
    <p class="info-city">Singapore 073194</p>
    <p class="info-web">www.glimmerloft.com.sg/curtain-cleaning</p>
    <p class="info-mail">Email: enquiries@glimmerloft.com.sg</p>
    <p class="info-tel">Tel: +65 8614 2253</p>
  </footer>
</body>
</html>
```